Book Title: The Harbor's Lantern. Author Name: Marisol Thackeray

We are needing a cover, spine and back cover design for a poetry book that we are publishing called The Harbor's Lantern. We are looking for an elegant, and simplistic design with a very natural, dynamic and powerful impact.

Design Idea #1 - Shiva Conch Shell with a pink or black background. See Glen Parvey Image attached for design inspiration. Simple and dynamic .
Title and Author name created in same style as the attached Glen Parvey's Lanterns and Driftwood image.

Design Idea #2 - Image of cauldron on (see cauldrons attached for ideas) black background.
See Glen Parvey Image attached for design inspiration. Simple and dynamic Title and Author name created in same style as the attached Glen Parvey's Lanterns and Driftwood image

Design Idea #3 - Image of Tree of Life (see attached images for idea of what we are looking for) Would like to see on plain white, green, black and green background.

Target Market(s)

Spiritual Women, healers, visionaries,Goddess'

Requirements
Must have
• Please see project descriptions for specific design concepts we are looking for. Please include the authors name: Marisol Thackeray on front, spine and back cover of the book

```html
<!DOCTYPE html>
<html lang="en">
<head>
<meta charset="utf-8">
<title>The Harbor’s Lantern — Cover Spread</title>
<link rel="stylesheet" href="https://fonts.googleapis.com/css2?family=Marcellus&family=EB+Garamond&display=swap">
<style>
  :root {
    --page: #ffffff;
    --cover: #151516;
    --ink: #ffffff;
    --spine-rule: #5a5a5c;
    --shell-light: #f4f2ef;
    --shell-mid: #e6d2bf;
    --shell-shadow: #b79a83;
    --code-box: #ffffff;
  }
  * { margin: 0; padding: 0; box-sizing: border-box; }
  html, body {
    width: 1200px; height: 1000px; overflow: hidden;
    background: var(--page);
  }
  .spread {
    position: absolute; left: 98px; top: 129px;
    width: 1003px; height: 742px;
    background: var(--cover);
  }
  .panel { position: absolute; top: 0; height: 100%; }
  .back { left: 0; width: 480px; }
  .spine {
    left: 480px; width: 43px;
    border-left: 1px solid var(--spine-rule);
    border-right: 1px solid var(--spine-rule);
  }
  .front { left: 523px; width: 480px; }

  .title {
    position: absolute; left: 0; width: 100%;
    text-align: center; color: var(--ink);
    font-family: "Marcellus", serif; font-weight: 400;
    font-size: 38px; line-height: 44px; letter-spacing: 0.2em;
    padding-left: 0.2em;
  }
  .back .title { top: 104px; left: 4px; }
  .front .title { top: 556px; }

  .author {
    position: absolute; left: 0; top: 96px; width: 100%;
    text-align: center; color: var(--ink);
    font-family: "Marcellus", serif; font-size: 44px;
    line-height: 51px; letter-spacing: 0.03em;
  }

  .back-author {
    position: absolute; left: 0; top: 500px; width: 100%;
    text-align: center; color: var(--ink);
    font-family: "Marcellus", serif; font-size: 15px;
    line-height: 20px; letter-spacing: 0.12em;
    padding-left: 6px;
  }

  .shell {
    position: absolute;
    border-radius: 50% 50% 46% 54% / 70% 70% 30% 30%;
    background: radial-gradient(ellipse at 62% 62%, var(--shell-light) 0%, var(--shell-light) 35%, var(--shell-mid) 70%, var(--shell-shadow) 100%);
  }
  .back .shell { left: 208px; top: 225px; width: 50px; height: 80px; }
  .front .shell { left: 178px; top: 279px; width: 124px; height: 200px; }

  .blurb {
    position: absolute; left: 0; top: 350px; width: 100%;
    list-style: none; text-align: center; color: var(--ink);
    font-family: "EB Garamond", serif; font-size: 9.5px; line-height: 24.3px;
    padding-left: 6px;
  }

  .code-box {
    position: absolute; left: 280px; top: 610px;
    width: 175px; height: 106px; background: var(--code-box);
  }

  .spine-text {
    position: absolute; left: 50%; color: var(--ink);
    font-family: "Marcellus", serif; white-space: nowrap;
    transform-origin: 0 0; transform: rotate(90deg) translateY(-50%);
  }
  .spine-title { top: 71px; font-size: 19px; letter-spacing: 0.2em; }
  .spine-author { top: 431px; font-size: 20px; letter-spacing: 0.02em; }
</style>
</head>
<body>
  <main class="spread">
    <section class="panel back">
      <h2 class="title">The Harbor’s<br>Lantern</h2>
      <div class="shell" role="img" aria-label="Photograph of a white conch shell"></div>
      <ul class="blurb">
        <li>Lorem ipsum dolor sit amet, consectetur adipiscing elit.</li>
        <li>Aenean suscipit egestas tellus eu condimentum.</li>
        <li>Donec hendrerit tortor porta tellus mollis iaculis.</li>
        <li>Curabitur volutpat metus est, vel maximus quam volutpat vitae.</li>
        <li>Aliquam et lectus faucibus, mattis libero id, interdum dui.</li>
      </ul>
      <p class="back-author">MARISOL THACKERAY</p>
      <div class="code-box"></div>
    </section>

    <section class="panel spine">
      <span class="spine-text spine-title">The Harbor’s Lantern</span>
      <span class="spine-text spine-author">MARISOL THACKERAY</span>
    </section>

    <section class="panel front">
      <p class="author">MARISOL<br>THACKERAY</p>
      <div class="shell" role="img" aria-label="Photograph of a white conch shell"></div>
      <h1 class="title">The Harbor’s<br>Lantern</h1>
    </section>
  </main>
</body>
</html>
```